Business Card Design Project

"Crestline Record Services" is database management company working in the direct marketing & digital printing industries. Currently going through a name & rebranding process we require a new company business card.

Industry/Entity Type

Marketing

```html
<!DOCTYPE html>
<html lang="en">
<head>
<meta charset="utf-8">
<title>Crestline Record Services – Business Card</title>
<link rel="stylesheet" href="https://fonts.googleapis.com/css2?family=Montserrat:wght@700&family=Questrial&display=swap">
<style>
  :root {
    --page: #ffffff;
    --sky: #1fc0ea;
    --sky-deep: #17a9d3;
    --band: #2b6c84;
    --band-dark: #1d4f63;
    --band-edge: #bff2ff;
    --ink: #3c5064;
    --frame: #3f5a66;
    --ornament: #8c8a78;
    --ornament-dark: #5f5e52;
    --white: #ffffff;
  }
  * { box-sizing: border-box; margin: 0; padding: 0; }
  html, body { width: 1000px; height: 1200px; overflow: hidden; background: var(--page); }
  body { position: relative; font-family: "Questrial", sans-serif; }

  .card { position: absolute; left: 8px; width: 984px; height: 560px; }
  .card--front { top: 28px; }
  .card--back { top: 612px; }

  .card__band { position: absolute; left: 0; width: 100%; height: 24px;
    background: linear-gradient(180deg, var(--band) 0%, var(--band-dark) 100%); }
  .card__band--top { top: 0; border-bottom: 3px solid var(--band-edge); }
  .card__band--bottom { bottom: 0; border-top: 3px solid var(--band-edge); }

  .card__field { position: absolute; left: 0; top: 27px; width: 100%; height: 506px;
    background: radial-gradient(ellipse at 30% 60%, var(--sky-deep) 0%, var(--sky) 55%, var(--sky) 100%); }

  .card__frame { position: absolute; left: 0; top: 0; width: 984px; height: 560px; }

  .brand { position: absolute; display: flex; align-items: center; color: var(--ink); }
  .brand__mark { background: var(--ink); flex: none; }
  .brand__name { font-family: "Questrial", sans-serif; font-weight: 400; line-height: 0.95; color: var(--ink); }

  .card--front .brand { left: 120px; top: 92px; }
  .card--front .brand__mark { width: 74px; height: 74px; margin-right: 20px; }
  .card--front .brand__name { font-size: 46px; }

  .card--back .brand { left: 92px; top: 150px; }
  .card--back .brand__mark { width: 160px; height: 160px; margin-right: 34px; }
  .card--back .brand__name { font-size: 78px; }

  .glow { color: var(--white); text-shadow: 0 0 4px rgba(255,255,255,0.7), 1px 1px 2px rgba(0,60,90,0.6); }

  .person { position: absolute; left: 512px; top: 262px; }
  .person__name { font-family: "Montserrat", sans-serif; font-weight: 700; font-size: 38px; letter-spacing: 0.5px; }
  .person__role { font-size: 20px; margin-top: 6px; margin-left: 4px; letter-spacing: 0.3px; }

  .contact { position: absolute; left: 516px; top: 410px; font-size: 18px; line-height: 23px; }
  .contact__web { font-size: 20px; }

  .card--back .web { position: absolute; left: 272px; top: 352px; font-size: 25px; letter-spacing: 0.3px; }
</style>
</head>
<body>

<section class="card card--front" aria-label="Business card front">
  <div class="card__band card__band--top"></div>
  <div class="card__field" role="img" aria-label="Sky blue background with faint floral swirls and dots"></div>
  <svg class="card__frame" viewBox="0 0 984 560" aria-hidden="true">
    <g stroke="var(--frame)" stroke-width="3" fill="none">
      <line x1="22" y1="95" x2="22" y2="500"/>
      <line x1="34" y1="120" x2="34" y2="480"/>
      <line x1="150" y1="478" x2="440" y2="478"/>
      <line x1="130" y1="492" x2="410" y2="492"/>
      <line x1="540" y1="66" x2="880" y2="66"/>
      <line x1="560" y1="80" x2="860" y2="80"/>
      <line x1="948" y1="150" x2="948" y2="470"/>
      <line x1="960" y1="130" x2="960" y2="490"/>
    </g>
    <rect x="14" y="318" width="230" height="206" rx="40" fill="url(#ornamentFront)" opacity="0.9" role="img" aria-label="Ornamental bubble corner cluster"/>
    <rect x="790" y="38" width="190" height="220" rx="40" fill="url(#ornamentFront)" opacity="0.9" role="img" aria-label="Ornamental bubble corner cluster"/>
    <defs>
      <radialGradient id="ornamentFront">
        <stop offset="0%" stop-color="var(--ornament)"/>
        <stop offset="100%" stop-color="var(--ornament-dark)" stop-opacity="0"/>
      </radialGradient>
    </defs>
  </svg>

  <div class="brand">
    <span class="brand__mark"></span>
    <span class="brand__name">Crestline<br>Record Services</span>
  </div>

  <div class="person">
    <p class="person__name glow">MARLOW.T</p>
    <p class="person__role glow">ART DESIGNER</p>
  </div>

  <div class="contact glow">
    <p>Tel. No.: 0400 318 265</p>
    <p>Email: marlow.t@crestlinerecords.com.au</p>
    <p class="contact__web">www.crestlinerecords.com.au</p>
  </div>
  <div class="card__band card__band--bottom"></div>
</section>

<section class="card card--back" aria-label="Business card back">
  <div class="card__band card__band--top"></div>
  <div class="card__field" role="img" aria-label="Sky blue background with faint floral swirls and dots"></div>
  <svg class="card__frame" viewBox="0 0 984 560" aria-hidden="true">
    <g stroke="var(--frame)" stroke-width="3" fill="none">
      <line x1="22" y1="95" x2="22" y2="500"/>
      <line x1="34" y1="120" x2="34" y2="480"/>
      <line x1="150" y1="478" x2="440" y2="478"/>
      <line x1="130" y1="492" x2="410" y2="492"/>
      <line x1="540" y1="66" x2="880" y2="66"/>
      <line x1="560" y1="80" x2="860" y2="80"/>
      <line x1="948" y1="150" x2="948" y2="470"/>
      <line x1="960" y1="130" x2="960" y2="490"/>
    </g>
    <rect x="14" y="318" width="230" height="206" rx="40" fill="url(#ornamentBack)" opacity="0.9" role="img" aria-label="Ornamental bubble corner cluster"/>
    <rect x="790" y="38" width="190" height="220" rx="40" fill="url(#ornamentBack)" opacity="0.9" role="img" aria-label="Ornamental bubble corner cluster"/>
    <defs>
      <radialGradient id="ornamentBack">
        <stop offset="0%" stop-color="var(--ornament)"/>
        <stop offset="100%" stop-color="var(--ornament-dark)" stop-opacity="0"/>
      </radialGradient>
    </defs>
  </svg>

  <div class="brand">
    <span class="brand__mark"></span>
    <span class="brand__name">Crestline<br>Record Services</span>
  </div>

  <p class="web glow">www.crestlinerecords.com.au</p>
  <div class="card__band card__band--bottom"></div>
</section>

</body>
</html>
```